Need updated stationery design for chiropractic clinic

We recently moved our office and are looking to refresh our letterhead, business cards, presentation folder and envelopes. I tend to prefer simple, clean designs. We communicate with a lot of attorneys and want to exude professionalism. I have attached our logo and 2 additional versions (all white and white letters instead of grey).

Target Market(s)

Other medical professionals and attorneys. Business cards will go to patients as well.

Industry/Entity Type

Healthcare

```html
<!DOCTYPE html>
<html lang="en">
<head>
<meta charset="utf-8">
<title>Meridian Spine – Business Card</title>
<link rel="stylesheet" href="https://fonts.googleapis.com/css2?family=Arimo:wght@400;700&family=Roboto+Condensed:wght@400&family=Open+Sans:wght@400;600&display=swap">
<style>
  :root {
    --page-bg: #e4e4e4;
    --card-blue-top: #0899c9;
    --card-blue-bottom: #0586b7;
    --card-white: #f6f6f7;
    --text-white: #ffffff;
    --brand-blue: #0a96c8;
    --brand-teal: #17c2cf;
    --text-grey: #4f4f52;
  }
  * { margin: 0; padding: 0; box-sizing: border-box; }
  html, body {
    width: 1200px; height: 1200px; overflow: hidden;
    background: var(--page-bg);
  }
  .canvas { position: relative; width: 1200px; height: 1200px; }
  .card {
    position: absolute; left: 262px; width: 686px; height: 392px;
    border-radius: 20px;
    box-shadow: 0 22px 30px rgba(0,0,0,0.22);
  }
  .card--front {
    top: 165px;
    background: linear-gradient(180deg, var(--card-blue-top), var(--card-blue-bottom));
    color: var(--text-white);
    font-family: "Arimo", Arial, sans-serif;
  }
  .card--back { top: 653px; background: var(--card-white); }

  .person { position: absolute; left: 58px; top: 86px; }
  .person__name { font-weight: 700; font-size: 24px; line-height: 1.1; }
  .person__role {
    font-family: "Roboto Condensed", "Arial Narrow", sans-serif;
    font-size: 16px; margin-top: 2px;
  }
  .address { position: absolute; left: 56px; top: 176px; font-size: 15.5px; line-height: 19px; }
  .contacts { position: absolute; left: 56px; top: 227px; list-style: none; font-size: 15.5px; }
  .contacts li { display: flex; align-items: center; height: 19.5px; }
  .contacts svg { width: 13px; height: 13px; margin-right: 12px; fill: var(--text-white); flex: none; }

  .brand {
    position: absolute; left: 0; right: 0; top: 148px;
    display: flex; justify-content: center; align-items: center; gap: 18px;
  }
  .brand__dot { width: 60px; height: 60px; border-radius: 50%; background: var(--brand-teal); flex: none; }
  .brand__name {
    font-family: "Open Sans", Arial, sans-serif; font-weight: 600;
    font-size: 50px; line-height: 1; color: var(--brand-blue); letter-spacing: -0.5px;
  }
  .brand__tagline {
    font-family: "Open Sans", Arial, sans-serif; font-weight: 400;
    font-size: 28px; line-height: 1; color: var(--text-grey); margin-top: 6px;
  }
</style>
</head>
<body>
<div class="canvas">
  <section class="card card--front">
    <div class="person">
      <div class="person__name">Daniel Brooks</div>
      <div class="person__role">Founder &amp; CEO</div>
    </div>
    <div class="address">4120 Cedar Ridge Road<br>Fairbanks, Alaska 99701</div>
    <ul class="contacts">
      <li><svg viewBox="0 0 16 16"><path d="M3.5 1l2.5 3-1.5 2c1 2 3 4 5 5l2-1.5 3 2.5-1.5 2.5C7 15 1 9 1 2.5z"/></svg>555-201-4837</li>
      <li><svg viewBox="0 0 16 16"><path d="M4 0h8v16H4zM5.5 2v10h5V2zM7 13.2h2v1.3H7z" fill-rule="evenodd"/></svg>555-318-9062</li>
      <li><svg viewBox="0 0 16 16"><path d="M4 1h8v4H4zM1 6h14v7h-2v-3H3v3H1zM4 11h8v4H4z"/></svg>555-746-2190</li>
      <li><svg viewBox="0 0 16 16"><path d="M1 3h14v10H1zM2.5 4.5L8 9l5.5-4.5"/></svg>hello@meridianspine.com</li>
      <li><svg viewBox="0 0 16 16"><circle cx="8" cy="8" r="7"/></svg>www.meridianspine.com</li>
    </ul>
  </section>

  <section class="card card--back">
    <div class="brand">
      <div class="brand__dot"></div>
      <div>
        <div class="brand__name">Meridian Spine</div>
        <div class="brand__tagline">INJURY CARE CLINIC</div>
      </div>
    </div>
  </section>
</div>
</body>
</html>
```